Web Design For Metal Recycling Company

We are a scrap and recycling company dealing mainly in scrap metal base in Singapore. We deal in both domestic market and international market. Currently we are still unsure if we want to have a "lively" or "professional" company image so we will leave it to the designer to deem what is good.

We wish for a website to be able to "Retain" the interest of new visitor and at the same time able to give enough information for new and existing customer. We would also wish for design that will get the visitor to "Engage" us.

The attached is the logo for the company and we would want to incorporate that into the website. Either of the logo is fine.

```html
<!DOCTYPE html>
<html lang="en">
<head>
<meta charset="utf-8">
<title>Kian Tat Metals – Industrial Scrap Recycling</title>
<link href="https://fonts.googleapis.com/css2?family=Open+Sans:wght@400;600;700&display=swap" rel="stylesheet">
<style>
:root{
  --gold:#c8962a;
  --gold-dark:#b5851f;
  --ink:#222222;
  --body:#444444;
  --muted:#666666;
  --header-bg:#1c1c1c;
  --footer-bg:#0b0b0b;
  --white:#ffffff;
  --badge:#8a8a8a;
}
*{margin:0;padding:0;box-sizing:border-box}
html,body{width:1191px;height:1200px;overflow:hidden;background:var(--white)}
body{font-family:"Open Sans",Arial,sans-serif;color:var(--body)}
.page{position:relative;width:1191px;height:1200px}
.abs{position:absolute}

/* header */
.site-header{position:absolute;left:0;top:0;width:1191px;height:128px;background:linear-gradient(180deg,#232323,#161616);border-bottom:1px solid #2a2a2a}
.brand{position:absolute;left:177px;top:13px;width:190px;text-align:center}
.brand-mark{display:block;width:54px;height:52px;margin:0 auto 11px;border:3px solid var(--gold)}
.brand-name{font-weight:700;font-size:19px;letter-spacing:1.5px;color:var(--gold);line-height:22px}
.call{position:absolute;right:189px;top:16px;font-size:20px;color:var(--gold);font-weight:600}
.call strong{font-weight:700}
.search{position:absolute;left:754px;top:52px;width:249px;height:21px;background:var(--white);border:1px solid #ccc;font-size:10px;color:#999;font-style:italic;padding:3px 6px}
.search svg{position:absolute;right:6px;top:3px}
.main-nav{position:absolute;top:97px;left:0;width:1191px;height:31px}
.main-nav a{position:absolute;color:var(--white);text-decoration:none;font-size:13.5px;white-space:nowrap}
.main-nav a.active::after{content:"";position:absolute;left:0;right:0;top:27px;height:3px;background:var(--gold)}

/* hero */
.hero{position:absolute;left:0;top:128px;width:1191px;height:351px;background:radial-gradient(ellipse at 50% 40%,#3a3a3a 0%,#262626 55%,#141414 100%)}
.hero h1{position:absolute;left:0;top:67px;width:1191px;text-align:center;font-weight:700;font-size:39px;line-height:47px;color:var(--gold);letter-spacing:.5px;text-shadow:0 2px 4px rgba(0,0,0,.6)}
.hero p{position:absolute;left:0;top:169px;width:1171px;text-align:center;font-size:15.5px;line-height:23px;color:#eeeeee}
.dots{position:absolute;left:557px;top:324px;display:flex;gap:6px}
.dots span{width:13px;height:13px;border-radius:50%;border:2px solid #ddd}
.dots span.on{background:var(--gold)}

/* offer */
.offer-title{position:absolute;left:0;top:515px;width:1171px;text-align:center;font-size:24px;font-weight:600;color:var(--gold)}
.offer-lead{position:absolute;left:0;top:557px;width:1171px;text-align:center;font-size:15.5px;line-height:23px;color:var(--body)}
.rule{position:absolute;left:493px;top:624px;width:205px;height:2px;background:var(--gold)}
.service{position:absolute;top:674px;width:270px;text-align:center}
.service .icon{display:block;margin:0 auto;width:85px;height:85px}
.service h3{margin-top:13px;font-size:15.5px;font-weight:700;color:var(--ink);letter-spacing:.3px}
.service p{margin-top:9px;font-size:12px;line-height:20px;color:var(--muted)}
.btn{display:inline-block;margin-top:14px;width:79px;height:23px;line-height:23px;background:var(--gold);color:var(--white);font-size:11px;text-decoration:none}

/* members */
.members-title{position:absolute;left:184px;top:957px;font-size:16.5px;font-weight:600;color:var(--gold)}
.badge{position:absolute;background:var(--badge);opacity:.75}

/* footer */
.site-footer{position:absolute;left:0;top:1089px;width:1191px;height:111px;background:var(--footer-bg);color:var(--white)}
.site-footer h4{position:absolute;font-size:13px;font-weight:700;letter-spacing:.3px}
.links{position:absolute;top:36px;list-style:none;font-size:11px;line-height:18px}
.contact{position:absolute;left:617px;top:38px;font-size:11px;line-height:17px}
.foot-mark{position:absolute;left:894px;top:18px;width:54px;height:53px;border:3px solid var(--gold)}
.rights{position:absolute;left:857px;top:83px;font-size:11px}
</style>
</head>
<body>
<div class="page">

  <header class="site-header">
    <div class="brand">
      <span class="brand-mark"></span>
      <div class="brand-name">KIAN TAT METALS</div>
    </div>
    <div class="call">Call Now : <strong>+800-555-0142</strong></div>
    <div class="search">Search
      <svg width="18" height="14" viewBox="0 0 18 14"><circle cx="6" cy="6" r="4" fill="none" stroke="#c8962a" stroke-width="2"/><line x1="9" y1="9" x2="16" y2="13" stroke="#c8962a" stroke-width="2.5"/></svg>
    </div>
    <nav class="main-nav">
      <a style="left:417px" href="#">HOME</a>
      <a class="active" style="left:498px" href="#">ABOUT US</a>
      <a style="left:597px" href="#">SERVICES</a>
      <a style="left:675px" href="#">BUY &amp; SELL SCRAP</a>
      <a style="left:818px" href="#">RECYCLING</a>
      <a style="left:925px" href="#">CONTACT US</a>
    </nav>
  </header>

  <section class="hero" role="img" aria-label="Dark photograph of a pile of industrial scrap metal">
    <h1>EFFICIENT INDUSTRIAL SCRAP<br>COLLECTION &amp; PROCCESSING</h1>
    <p>Lorem ipsum dolor sit amet, consectetur adipisicing elit, sed do eiusmod<br>tempor aute irure dolor in reprehenderit in voluptate velit esse cillum<br>dolore eu fugiat lorem ipsum dolor nulla pariatur.</p>
    <div class="dots"><span></span><span class="on"></span><span></span><span></span></div>
  </section>

  <h2 class="offer-title">WHAT WE OFFER</h2>
  <p class="offer-lead">Kian Tat Metals specializes in recycling ferrous &amp; non-ferrous metals for industrial use.<br>Our customers include steel mills, foundries and trading houses.</p>
  <div class="rule"></div>

  <div class="service" style="left:179px">
    <svg class="icon" viewBox="0 0 85 85"><rect x="1.5" y="1.5" width="82" height="82" fill="none" stroke="#c8962a" stroke-width="3"/>
      <g fill="#c8962a"><path d="M36 20h13l8 13 5-3-4 14-13-3 5-3-6-10-7 12-7-4z"/><path d="M22 47l7-12 6 3-5 9h13v-6l10 10-10 10v-6H28z"/><path d="M57 62l8-14 6 4-7 12z"/></g></svg>
    <h3>PRODUCTS WE RECYCLE</h3>
    <p>We recycle Ferrous, Aluminium, Stainless Steel,<br>Cable wire, Cooper, Brass &amp; others</p>
    <a class="btn" href="#">Learn More</a>
  </div>

  <div class="service" style="left:458px">
    <svg class="icon" viewBox="0 0 85 85"><rect x="1.5" y="1.5" width="82" height="82" fill="none" stroke="#c8962a" stroke-width="3"/>
      <g fill="#c8962a"><path d="M22 34h28v-9l16 14H22z"/><path d="M63 46H35v9L19 41h44z"/></g></svg>
    <h3>SCRAP METAL TRADING</h3>
    <p>We also Buy and Sell Scrap Materials like<br>Copper, Brass, CableWire, Iron &amp; more</p>
    <a class="btn" href="#">Learn More</a>
  </div>

  <div class="service" style="left:732px">
    <svg class="icon" viewBox="0 0 85 85"><rect x="1.5" y="1.5" width="82" height="82" fill="none" stroke="#c8962a" stroke-width="3"/>
      <g fill="#c8962a"><path d="M42 13a29 29 0 1 0 27 37l-7-2a21 21 0 1 1-4-20l-6 4 17 5-1-17-5 5A29 29 0 0 0 42 13z"/><path d="M36 36c-4 6-6 8-6 11a6 6 0 0 0 12 0c0-3-2-5-6-11z"/><path d="M50 33c-4 6-6 8-6 11a6 6 0 0 0 12 0c0-3-2-5-6-11z"/></g></svg>
    <h3>PROPER WASTE DISPOSAL</h3>
    <p>We take Good Care of the Environment will help<br>you separate your material for proper disposal</p>
    <a class="btn" href="#">Learn More</a>
  </div>

  <h2 class="members-title">PROUD MEMBER OF INTERNATIONAL RECYCLING GROUP</h2>
  <div class="badge" style="left:234px;top:1005px;width:102px;height:42px;border-radius:4px"></div>
  <div class="badge" style="left:421px;top:1002px;width:143px;height:46px;border-radius:4px"></div>
  <div class="badge" style="left:644px;top:993px;width:64px;height:64px;border-radius:50%;background:#5aa33c"></div>
  <div class="badge" style="left:784px;top:1006px;width:160px;height:44px;border-radius:4px"></div>

  <footer class="site-footer">
    <h4 style="left:168px;top:19px">PAGES</h4>
    <ul class="links" style="left:168px"><li>Home</li><li>About Us</li><li>Terms and Conditions</li></ul>
    <ul class="links" style="left:324px"><li>Privacy Policy</li><li>Membership</li><li>Recycling</li></ul>
    <ul class="links" style="left:458px"><li>Contact</li><li>Scrap Prices</li><li>Site Disclaimer</li></ul>
    <h4 style="left:617px;top:20px">CONTACT DETAILS</h4>
    <div class="contact">p: +65 555 0190 &nbsp;f: +65 555 0191<br>PO Box 48, Tuas Harbour Lane<br>Westport City, 6390</div>
    <div class="foot-mark"></div>
    <div class="rights">All Rights Reserved © 2014</div>
  </footer>

</div>
</body>
</html>
```